Ridgeline Yard Works Stationary Package
Business Cards, Letterhead, Envelope, Sticker, Fax Cover sheet, invoice, and estimate
Ridgeline Yard Works Stationary Package - Construction
Creative Brief
Use same font as used in my logo
Pete Marrow
Owner
4172 W. Fenwick Rd. Burbank, IL 60421
petemarrow@quailnet.example
www.ridgelineyardworks.example
Can information be in a format that can be edited for future use. ex: Name Changes, New Numbers, etc?

```html
<!DOCTYPE html>
<html lang="en">
<head>
<meta charset="utf-8">
<title>Ridgeline Yard Works – Business Card</title>
<link rel="stylesheet" href="https://fonts.googleapis.com/css2?family=Arimo:wght@400;700&display=swap">
<style>
  :root {
    --page-bg: #e9e6e1;
    --card-white: #ffffff;
    --ink-dark: #1d1d1f;
    --ink-grey: #3a3a3c;
    --divider-red: #9b1c1f;
    --blue-glow: #1d7fd6;
    --blue-mid: #17469a;
    --blue-deep: #121a52;
    --text-light: #ffffff;
    --mark-square: #2c6fb8;
  }
  * { margin: 0; padding: 0; box-sizing: border-box; }
  html, body {
    width: 1200px; height: 778px; overflow: hidden;
    background: var(--page-bg);
    font-family: "Arimo", Arial, sans-serif;
  }
  .card {
    position: absolute;
    left: 120px; top: 139px;
    width: 960px; height: 500px;
    border-radius: 34px;
    overflow: hidden;
    display: flex;
  }
  .card-front {
    width: 482px; height: 100%;
    background: var(--card-white);
    position: relative;
  }
  .card-divider {
    width: 4px; height: 100%;
    background: var(--divider-red);
    border-left: 1px solid #fff;
  }
  .card-back {
    flex: 1; height: 100%;
    position: relative;
    background: radial-gradient(ellipse 62% 58% at 50% 48%, var(--blue-glow) 0%, var(--blue-mid) 48%, var(--blue-deep) 100%);
    color: var(--text-light);
  }
  .brand {
    position: absolute;
    left: 0; right: 0; top: 168px;
    text-align: center;
  }
  .brand-square {
    width: 80px; height: 80px;
    margin: 0 auto 18px;
    background: var(--mark-square);
    border-radius: 14px;
  }
  .brand-name {
    font-weight: 700;
    font-size: 38px;
    color: var(--ink-dark);
    letter-spacing: -0.3px;
  }
  .brand-tagline {
    display: flex; align-items: center; justify-content: center;
    gap: 10px;
    margin-top: 4px;
    font-size: 16px;
    color: var(--ink-grey);
  }
  .brand-tagline::before, .brand-tagline::after {
    content: ""; width: 46px; height: 2px; background: var(--ink-grey);
  }
  .contact {
    position: absolute;
    left: 62px; top: 72px;
  }
  .contact-name { font-weight: 700; font-size: 27px; line-height: 30px; }
  .contact-role { font-weight: 700; font-size: 21px; line-height: 28px; }
  .contact-address { margin-top: 56px; font-size: 21px; line-height: 33px; }
  .contact-lines { margin-top: 36px; list-style: none; font-size: 21px; }
  .contact-lines li {
    display: flex; align-items: center; gap: 12px;
    height: 32px;
  }
  .contact-lines svg { width: 18px; height: 18px; flex: none; fill: var(--text-light); }
</style>
</head>
<body>
  <div class="card">
    <section class="card-front">
      <div class="brand">
        <div class="brand-square"></div>
        <div class="brand-name">Ridgeline Yard Works</div>
        <div class="brand-tagline">Home Restoration Specialists</div>
      </div>
    </section>
    <div class="card-divider"></div>
    <section class="card-back">
      <div class="contact">
        <div class="contact-name">Pete Marrow</div>
        <div class="contact-role">Owner</div>
        <div class="contact-address">4172 W. Fenwick Rd.<br>Burbank, IL 60421</div>
        <ul class="contact-lines">
          <li>
            <svg viewBox="0 0 18 18" aria-hidden="true"><rect x="5" y="1" width="8" height="16" rx="1.5"/><rect x="6.5" y="3" width="5" height="9" fill="#17469a"/></svg>
            (708) 555-0142
          </li>
          <li>
            <svg viewBox="0 0 18 18" aria-hidden="true"><rect x="5" y="1" width="8" height="5"/><rect x="1" y="6" width="16" height="7" rx="1.5"/><rect x="5" y="11" width="8" height="6"/></svg>
            (708) 555-0187
          </li>
          <li>
            <svg viewBox="0 0 18 18" aria-hidden="true"><rect x="1" y="3.5" width="16" height="11" rx="1"/><path d="M1.5 4.5 L9 10 L16.5 4.5" fill="none" stroke="#17469a" stroke-width="1.5"/></svg>
            petemarrow@quailnet.example
          </li>
          <li>
            <svg viewBox="0 0 18 18" aria-hidden="true"><circle cx="9" cy="9" r="8"/><path d="M1 9 H17 M9 1 C5 5 5 13 9 17 M9 1 C13 5 13 13 9 17" fill="none" stroke="#17469a" stroke-width="1.3"/></svg>
            www.ridgelineyardworks.example
          </li>
        </ul>
      </div>
    </section>
  </div>
</body>
</html>
```